Retractable Banners for Ridgeway Talent Alliance

We need to have 2 different retractable banners designed that will be used at a variety of events. We plan to have the banners printed through printovera.com. According to their site, specs are as follows:

Retractable banners are digitally printed on 12oz double-sided smooth vinyl. While the area on the retractable banners is 33 x 78, the customer will want to provide a file that has an area of 35 x 82 to account for bleed, with 3" of that vertical bleed at the bottom of the design. Recommended DPI is 150. Upload capacity for Retractable Banners is 100MP.

Banner #1:
Ridgeway Talent Alliance logo at top

Then the following text placed lower on the banner:

Creating Positive Impacts for Cedar Valley Businesses (Heading)

Body of text: Ridgeway Talent Alliance is committed to enhancing the region's ability to meet the workforce needs of local employers through the investments of federal and state funds.

Banner #2:

Meeting the workforce needs of employers and individuals through partnerships and innovation.

You can check out some of our images (water drop, waves) and color schemes we use on our website at ridgewaytalent.org.

Target Market(s)

Job seekers, workforce development professionals, city leaders, company CEO's, community members, elected officials.

Industry/Entity Type

Events

Font styles to use
Serif
Sans Serif

Requirements
Must have
• -Be easy to read and understand
• - Must include Ridgeway Talent Alliance logo and text provided for each banner
Nice to have
• color ideas for banners: #0655a3; #0393ce; #00a990; #0355a3; #00a990; #33a6d7
Should not have
• Nothing that depicts gender

```html
<!DOCTYPE html>
<html lang="en">
<head>
<meta charset="utf-8">
<title>Ridgeway Talent Alliance – Retractable Banners</title>
<link href="https://fonts.googleapis.com/css2?family=Bebas+Neue&family=Oswald:wght@600&family=Roboto+Condensed:wght@700&display=swap" rel="stylesheet">
<style>
  :root {
    --stage: #7b7e83;
    --brand-blue: #0d55a6;
    --brand-teal: #0aa98f;
    --ink-black: #0b0b0d;
    --paper: #ffffff;
    --leaf-light: #b9d879;
    --leaf-mid: #6f9d3c;
    --leaf-deep: #33561f;
    --soil-dark: #1d2a20;
    --sprout-mid: #55704a;
  }
  * { margin: 0; padding: 0; box-sizing: border-box; }
  html, body { width: 1200px; height: 900px; overflow: hidden; }
  body { background: var(--stage); position: relative; }

  .banner {
    position: absolute;
    top: 60px;
    width: 320px;
    height: 766px;
    background: var(--paper);
    overflow: hidden;
  }
  .banner--partnerships { left: 216px; }
  .banner--impacts { left: 654px; }

  .banner__art { position: absolute; inset: 0; width: 320px; height: 766px; }

  .brand {
    position: absolute;
    top: 34px;
    left: 0;
    width: 320px;
    display: flex;
    align-items: center;
    justify-content: center;
    gap: 8px;
    color: var(--brand-blue);
    font-family: "Oswald", sans-serif;
    font-weight: 600;
    text-transform: uppercase;
  }
  .brand__dot { width: 28px; height: 28px; border-radius: 50%; background: var(--brand-blue); }
  .brand__name { display: flex; flex-direction: column; line-height: 1; }
  .brand__line-main { font-size: 17px; letter-spacing: 0.5px; }
  .brand__line-sub { font-size: 10px; letter-spacing: 5px; margin-top: 3px; }

  .headline {
    position: absolute;
    color: var(--paper);
    font-family: "Bebas Neue", sans-serif;
    font-weight: 400;
    font-size: 34px;
    line-height: 40px;
    text-transform: uppercase;
    letter-spacing: 0.4px;
  }
  .banner--partnerships .headline { left: 44px; top: 408px; text-align: left; }
  .banner--impacts .headline { right: 44px; top: 420px; text-align: right; }

  .mission {
    position: absolute;
    left: 50px;
    top: 626px;
    width: 220px;
    color: var(--paper);
    font-family: "Roboto Condensed", sans-serif;
    font-weight: 700;
    font-size: 12px;
    line-height: 18px;
    text-align: center;
  }
</style>
</head>
<body>

  <section class="banner banner--partnerships">
    <svg class="banner__art" viewBox="0 0 320 766" xmlns="http://www.w3.org/2000/svg">
      <defs>
        <linearGradient id="canopyTones" x1="0" y1="0" x2="1" y2="1">
          <stop offset="0" stop-color="var(--leaf-light)"/>
          <stop offset="0.5" stop-color="var(--leaf-mid)"/>
          <stop offset="1" stop-color="var(--leaf-deep)"/>
        </linearGradient>
      </defs>
      <rect x="0" y="100" width="320" height="566" fill="url(#canopyTones)" role="img" aria-label="Photo of green tree canopy seen from below"/>
      <rect x="0" y="90" width="320" height="10" fill="var(--brand-teal)"/>
      <polygon points="-4,154 150,302 -4,362" fill="var(--brand-teal)" stroke="var(--paper)" stroke-width="4"/>
      <polygon points="-4,466 150,302 324,474 324,666 -4,666" fill="var(--brand-blue)" stroke="var(--paper)" stroke-width="4"/>
      <rect x="0" y="666" width="320" height="100" fill="var(--ink-black)"/>
    </svg>

    <div class="brand">
      <span class="brand__dot"></span>
      <span class="brand__name">
        <span class="brand__line-main">Ridgeway Talent</span>
        <span class="brand__line-sub">Alliance</span>
      </span>
    </div>

    <h2 class="headline">Meeting the<br>workforce needs<br>of employers and<br>individuals through<br>partnerships and<br>innovations</h2>
  </section>

  <section class="banner banner--impacts">
    <svg class="banner__art" viewBox="0 0 320 766" xmlns="http://www.w3.org/2000/svg">
      <defs>
        <linearGradient id="sproutTones" x1="0" y1="0" x2="1" y2="1">
          <stop offset="0" stop-color="var(--sprout-mid)"/>
          <stop offset="0.6" stop-color="var(--soil-dark)"/>
          <stop offset="1" stop-color="#121812"/>
        </linearGradient>
      </defs>
      <rect x="0" y="100" width="320" height="510" fill="url(#sproutTones)" role="img" aria-label="Photo of a water drop falling onto a young green sprout"/>
      <rect x="0" y="90" width="320" height="10" fill="var(--brand-teal)"/>
      <polygon points="324,180 212,304 324,392" fill="var(--brand-teal)" stroke="var(--paper)" stroke-width="4"/>
      <polygon points="-4,522 212,326 324,432 324,610 -4,610" fill="var(--brand-blue)" stroke="var(--paper)" stroke-width="4"/>
      <rect x="0" y="610" width="320" height="156" fill="var(--ink-black)"/>
    </svg>

    <div class="brand">
      <span class="brand__dot"></span>
      <span class="brand__name">
        <span class="brand__line-main">Ridgeway Talent</span>
        <span class="brand__line-sub">Alliance</span>
      </span>
    </div>

    <h2 class="headline">Creating<br>positive impacts<br>for Cedar<br>Valley business</h2>

    <p class="mission">Ridgeway Talent Alliance is committed to enhancing the region's ability to meet the workforce needs of local employers through the investments of federal and state funds.</p>
  </section>

</body>
</html>
```